COVID-19 Related Signage for Hotel

Need to create new COVID-19 related signage utilizing our brand assets. Please use screenshots for copy/direction. essentially duplicate the screenshots but with our logo/branding.

All brand assets have been uploaded and examples of signage content. Pictures are not necessary but you can add them if you want similar to the examples attached.

Sign requirements

sign 1. Text "Hand Sanitizer Station" can add graphic
sign 2. Text "Protect Yourself" duplicate copy in the attached pictures
sign 3. Text "Face Mask Required" can add graphic
sign 4. Text "Face Covering Do's and Don'ts with text from "Face-covering checklist.jpg" REMOVE BWT logo or website or 3 face mask graphics
sign 5. Text "Maintain 6 Foot Distance" This sign will be printed and placed on the ground for guests to know where to stand in queue. Would prefer a circular Design. sign 6. Text "Wet, Lather, Scrub, Rinse, Dry" similar to screenshots attached.

ALL signs should have same look and feel throughout utilizing our brand graphics, logo, colors, and guidelines.

Target Market(s)

Hotel Guests

Industry/Entity Type

Hotel

Font styles to use
Sans Serif

Requirements
Must have
• Cohesive, unified branding look and feel

Should not have
• any use of the word "COVID-19" or Coronavirus.

```html
<!DOCTYPE html>
<html lang="en">
<head>
<meta charset="utf-8">
<title>Cedar Brook Lodge – Guest Health Signage</title>
<link href="https://fonts.googleapis.com/css2?family=Roboto+Condensed:wght@400;500&display=swap" rel="stylesheet">
<style>
  :root {
    --backdrop: #d6d6d6;
    --sign-white: #ffffff;
    --pattern-tint: #e6e6e6;
    --brand-orange: #f28a35;
    --ink-gray: #5b5b5b;
    --column-gray: #5e5e5e;
    --text-white: #ffffff;
  }
  * { box-sizing: border-box; margin: 0; padding: 0; }
  html, body { width: 1200px; height: 678px; overflow: hidden; }
  body {
    background: var(--backdrop);
    font-family: "Roboto Condensed", "Arial Narrow", sans-serif;
    position: relative;
  }
  .sign {
    position: absolute;
    width: 446px;
    height: 223px;
    background: var(--sign-white);
    overflow: hidden;
  }
  .sign--sanitizer { left: 137px; top: 110px; }
  .sign--handwash  { left: 602px; top: 110px; }
  .sign--protect   { left: 137px; top: 352px; }
  .sign--mask      { left: 602px; top: 354px; }

  .sign__pattern {
    position: absolute; inset: 0;
    background: linear-gradient(160deg, var(--pattern-tint) 0%, var(--pattern-tint) 35%, var(--sign-white) 80%);
  }
  .sign__band {
    position: absolute; left: 0; right: 0; bottom: 0;
    height: 20px;
    background: var(--brand-orange);
  }
  .sign__headline {
    position: absolute;
    color: var(--ink-gray);
    font-weight: 500;
    letter-spacing: -0.5px;
  }
  .sign--sanitizer .sign__headline,
  .sign--mask .sign__headline {
    left: 20px; top: 8px;
    font-size: 64px; line-height: 58px;
  }
  .sign--protect .sign__headline {
    left: 24px; top: 6px;
    font-size: 92px; line-height: 86px;
  }

  .brand-lockup {
    position: absolute;
    right: 16px; top: 16px;
    display: flex; align-items: center; gap: 6px;
    color: var(--ink-gray);
    font-size: 13px; font-weight: 400;
  }
  .brand-lockup__dot {
    width: 14px; height: 14px; border-radius: 50%;
    background: var(--brand-orange);
  }

  .step { position: absolute; bottom: 0; width: 89.2px; }
  .step__title {
    position: absolute; left: 2px;
    font-size: 32px; line-height: 1; font-weight: 400;
    transform: translateY(-100%);
    top: 0; padding-bottom: 2px;
    white-space: nowrap;
  }
  .step__body {
    height: 100%;
    padding: 18px 7px 0 8px;
    color: var(--text-white);
    font-size: 15px; line-height: 15.5px;
  }
  .step--orange .step__body { background: var(--brand-orange); }
  .step--orange .step__title { color: var(--brand-orange); }
  .step--gray .step__body { background: var(--column-gray); }
  .step--gray .step__title { color: var(--ink-gray); }
  .step--wet    { left: 0;       top: 41px;  }
  .step--lather { left: 89.2px;  top: 72px;  }
  .step--scrub  { left: 178.4px; top: 102px; }
  .step--rinse  { left: 267.6px; top: 132px; }
  .step--dry    { left: 356.8px; top: 161px; }
  .step--wet .step__title { left: 18px; }
  .step--dry .step__body { padding-top: 8px; }
</style>
</head>
<body>

  <section class="sign sign--sanitizer">
    <div class="sign__pattern" role="img" aria-label="Soft repeating swirl pattern in light gray"></div>
    <h1 class="sign__headline">Hand<br>Sanitizing<br>Station</h1>
    <div class="brand-lockup"><span class="brand-lockup__dot"></span><span>Cedar Brook Lodge</span></div>
    <div class="sign__band"></div>
  </section>

  <section class="sign sign--handwash">
    <div class="sign__pattern" role="img" aria-label="Soft repeating swirl pattern in light gray"></div>
    <div class="brand-lockup"><span class="brand-lockup__dot"></span><span>Cedar Brook Lodge</span></div>
    <div class="step step--orange step--wet">
      <h2 class="step__title">WET</h2>
      <p class="step__body">Wash with clean, running water</p>
    </div>
    <div class="step step--gray step--lather">
      <h2 class="step__title">LATHER</h2>
      <p class="step__body">Lather with soap, in between fingers, under nails &amp; all over hands</p>
    </div>
    <div class="step step--orange step--scrub">
      <h2 class="step__title">SCRUB</h2>
      <p class="step__body">Scrub for at least 20 seconds</p>
    </div>
    <div class="step step--gray step--rinse">
      <h2 class="step__title">RINSE</h2>
      <p class="step__body">Rinse with clean, running water</p>
    </div>
    <div class="step step--orange step--dry">
      <h2 class="step__title">DRY</h2>
      <p class="step__body">Dry with a clean towel or air dry</p>
    </div>
  </section>

  <section class="sign sign--protect">
    <div class="sign__pattern" role="img" aria-label="Soft repeating swirl pattern in light gray"></div>
    <h1 class="sign__headline">Protect<br>Yourself</h1>
    <div class="brand-lockup"><span class="brand-lockup__dot"></span><span>Cedar Brook Lodge</span></div>
    <div class="sign__band"></div>
  </section>

  <section class="sign sign--mask">
    <div class="sign__pattern" role="img" aria-label="Soft repeating swirl pattern in light gray"></div>
    <h1 class="sign__headline">Face<br>Mask<br>Required</h1>
    <div class="brand-lockup"><span class="brand-lockup__dot"></span><span>Cedar Brook Lodge</span></div>
    <div class="sign__band"></div>
  </section>

</body>
</html>
```